Wholesale in Gold Jewellery & Gold Bullion

We are an established gold jewellery and gold bullion wholesaler selling these products to international clients. We already have a name and logo of our company, hence please view attached current card design. We need a completely new design to compliment our business and industry and the final design should be new and elegant.

Contact Information for Business Card

New card details must be same as per current card. Like logo, name, tel no. & etc.

Colors

Designer to choose colors to be used in the design.

```html
<!DOCTYPE html>
<html lang="en">
<head>
<meta charset="utf-8">
<title>Varin &amp; Co – Business Card</title>
<link rel="stylesheet" href="https://fonts.googleapis.com/css2?family=Cinzel:wght@400;500&family=Source+Sans+3:wght@400&display=swap">
<style>
  :root {
    --backdrop: #5c5c5c;
    --card-white: #ffffff;
    --gold: #d9960f;
    --ink: #2b2b2b;
    --rule: #9a9a9a;
  }
  * { margin: 0; padding: 0; box-sizing: border-box; }
  html, body { width: 1200px; height: 802px; overflow: hidden; }
  body { background: var(--backdrop); position: relative; }

  .card {
    position: absolute;
    top: 274px;
    width: 442px;
    height: 264px;
    box-shadow: 2px 3px 6px rgba(0,0,0,0.35);
  }
  .card--front { left: 136px; background: var(--card-white); }
  .card--back { left: 624px; background: var(--gold); }

  .brand-dot {
    position: absolute;
    left: 71px; top: 71px;
    width: 78px; height: 78px;
    border-radius: 50%;
    background: var(--gold);
  }
  .brand-name {
    position: absolute;
    left: 0; width: 222px;
    top: 158px;
    text-align: center;
    font-family: "Cinzel", serif;
    font-weight: 500;
    font-size: 25px;
    color: var(--ink);
    letter-spacing: 0.5px;
  }

  .divider {
    position: absolute;
    left: 222px; top: 67px;
    width: 1px; height: 131px;
    background: var(--rule);
  }

  .contact {
    position: absolute;
    left: 238px; top: 63px;
    font-family: "Source Sans 3", sans-serif;
    color: var(--ink);
    font-size: 12.5px;
    line-height: 15.5px;
  }
  .contact__name {
    font-family: "Cinzel", serif;
    font-weight: 500;
    color: var(--gold);
    font-size: 15px;
    line-height: 17px;
    letter-spacing: 0.4px;
  }
  .contact__role { margin-bottom: 4px; }
  .contact__address { margin-bottom: 6px; }
  .contact__list { list-style: none; }
  .contact__list li { display: flex; align-items: center; height: 15.8px; }
  .contact__list svg { width: 11px; height: 11px; margin-right: 4px; fill: var(--gold); flex: none; }

  .back-name {
    position: absolute;
    left: 0; right: 0;
    top: 94px;
    text-align: center;
    font-family: "Cinzel", serif;
    font-weight: 400;
    font-size: 44px;
    color: var(--card-white);
    letter-spacing: 0.5px;
  }
</style>
</head>
<body>

<section class="card card--front">
  <div class="brand-dot" aria-hidden="true"></div>
  <div class="brand-name">VARIN &amp; CO</div>
  <div class="divider"></div>

  <div class="contact">
    <div class="contact__name">ARJUN KESAVAN</div>
    <div class="contact__role">Director</div>
    <div class="contact__address">14 Orchid Lane,<br>Singapore 208115</div>
    <ul class="contact__list">
      <li>
        <svg viewBox="0 0 12 12" aria-hidden="true"><path d="M1 4c0-2 2-3 5-3s5 1 5 3v1H8.5V3.8C7.8 3.5 4.2 3.5 3.5 3.8V5H1z"/><path d="M3 6h6l1.5 5h-9z"/></svg>
        +65 6420 1580
      </li>
      <li>
        <svg viewBox="0 0 12 12" aria-hidden="true"><path d="M3.5 0.5h5a1 1 0 0 1 1 1v9a1 1 0 0 1-1 1h-5a1 1 0 0 1-1-1v-9a1 1 0 0 1 1-1zM4 2v7h4V2z"/></svg>
        +65 9135 2246
      </li>
      <li>
        <svg viewBox="0 0 12 12" aria-hidden="true"><path d="M3 0.5h6v3H3z"/><path d="M1 4.5h10v4.5H9V7H3v2H1z"/><path d="M3.5 7.8h5v3.7h-5z"/></svg>
        +65 6420 1581
      </li>
      <li>
        <svg viewBox="0 0 12 12" aria-hidden="true"><path d="M0.5 2.5h11v7h-11z"/><path d="M0.8 2.8L6 7l5.2-4.2" fill="none" stroke="#fff" stroke-width="1"/></svg>
        arjun@varinco.com
      </li>
    </ul>
  </div>
</section>

<section class="card card--back">
  <div class="back-name">VARIN &amp; CO</div>
</section>

</body>
</html>
```